Birchway Swing Studio New Location Postcard

I need a postcard announcing our new location. It is a indoor golf training facility that offers award winner instruction, state-of-the-art technology, and custom club fitting. Whether you are a beginner, an aspiring athlete, or an amateur, Birchway Swing Studio offers personalized programs to help take your game to the next level. Call now to schedule your free tour or to sign up. Limited memberships available.
I would like somewhere are on postcard to say Don't put away your clubs just yet! The course may be closed but Birchway Swing Studio's new indoor location is open!
Industry/Entity Type
Training
Look and feel
Each slider illustrates characteristics of the customer's brand and the style your logo design should communicate.

```html
<!DOCTYPE html>
<html lang="en">
<head>
<meta charset="utf-8">
<title>Birchway Swing Studio – New Location Postcard</title>
<link href="https://fonts.googleapis.com/css2?family=Roboto+Condensed:ital,wght@0,400;0,700;1,400;1,700&display=swap" rel="stylesheet">
<style>
  :root {
    --brand-red: #d42a2a;
    --header-red: #c8232a;
    --ink: #111111;
    --link-blue: #2e4a9e;
    --stamp: #f6e3dc;
    --rule: #d4d4d4;
    --lawn: #8dc63f;
    --grass-dark: #4f8f1c;
    --grass-light: #7fbf36;
    --page: #e4e4e4;
    --paper: #ffffff;
  }
  * { margin: 0; padding: 0; box-sizing: border-box; }
  html, body { width: 1200px; height: 1200px; overflow: hidden; }
  body {
    background: var(--page);
    font-family: "Roboto Condensed", "Arial Narrow", sans-serif;
    color: var(--ink);
    position: relative;
  }
  .postcard {
    position: absolute;
    left: 238px;
    width: 724px;
    height: 561px;
    background: var(--paper);
    overflow: hidden;
  }
  .postcard--back { top: 30px; }
  .postcard--front { top: 610px; }
  .abs { position: absolute; }

  /* ---------- Back side ---------- */
  .brand-name {
    left: 43px; top: 38px;
    font-size: 40px; font-weight: 700; color: var(--brand-red);
    line-height: 1; white-space: nowrap;
  }
  .brand-tagline {
    left: 43px; top: 84px;
    font-size: 22px; font-weight: 700; font-style: italic; line-height: 1;
  }
  .offer-title {
    left: 43px; top: 120px;
    font-size: 21px; font-weight: 700; line-height: 1;
  }
  .offer-list {
    left: 43px; top: 150px; list-style: none;
    font-size: 17px; line-height: 25.5px;
  }
  .offer-list li { position: relative; padding-left: 19px; }
  .offer-list li::before {
    content: ""; position: absolute; left: 1px; top: 8px;
    width: 10px; height: 10px; border-radius: 50%; background: var(--brand-red);
  }
  .intro {
    left: 45px; top: 229px; width: 300px;
    font-size: 13.5px; line-height: 17px;
  }
  .cta {
    right: 382px; top: 304px; text-align: right;
    color: var(--brand-red); font-weight: 700; text-transform: uppercase;
    line-height: 18px;
  }
  .cta span { display: block; }
  .cta .cta-line1 { font-size: 13px; }
  .cta .cta-line2 { font-size: 14.5px; }
  .phone {
    right: 382px; top: 340px;
    font-size: 28px; font-weight: 700; line-height: 1;
  }
  .website {
    right: 382px; top: 390px;
    font-size: 16px; font-weight: 700; color: var(--link-blue); line-height: 1;
  }
  .note {
    right: 382px; top: 413px;
    font-size: 13.5px; color: #444; line-height: 1;
  }
  .golfer-art {
    left: 25px; top: 308px; width: 134px; height: 155px;
    background: linear-gradient(180deg, #f4f4f4 0%, #e2e2e2 100%);
  }
  .red-block {
    left: 18px; top: 463px; width: 73px; height: 98px;
    background: var(--brand-red);
  }
  .stamp {
    left: 560px; top: 33px; width: 130px; height: 131px;
    background: var(--stamp);
  }
  .address-line {
    left: 398px; width: 292px; height: 1px; background: var(--rule);
  }

  /* ---------- Front side ---------- */
  .photo-strip {
    left: 0; top: 90px; width: 44px; height: 225px;
    background: linear-gradient(180deg, #9a9a9a, #3a3a3a);
  }
  .lawn-panel {
    left: 44px; top: 80px; width: 244px; height: 235px;
    background: var(--lawn);
  }
  .scene-photo {
    left: 288px; top: 80px; width: 436px; height: 235px;
    background: linear-gradient(180deg, #8e8e8e 0%, #cfcfcf 45%, #5a5a5a 100%);
  }
  .grass {
    left: 0; top: 315px; width: 724px; height: 246px;
    background: linear-gradient(180deg, var(--grass-light) 0%, #6db02e 45%, var(--grass-dark) 100%);
  }
  .header-band { left: 0; top: 0; width: 724px; height: 130px; }
  .headline {
    left: 0; top: 22px; width: 724px; text-align: center;
    font-size: 41px; font-weight: 700; font-style: italic; color: #fff;
    line-height: 1; text-shadow: 0 2px 3px rgba(0,0,0,0.35);
  }
  .closing {
    left: 20px; top: 370px; width: 340px; text-align: center;
  }
  .closing-lead { font-size: 24px; line-height: 1; display: block; }
  .closing-name {
    font-size: 35px; font-weight: 700; font-style: italic;
    line-height: 1.15; display: block; white-space: nowrap;
  }
  .closing-tag {
    font-size: 25px; font-weight: 700; font-style: italic;
    line-height: 1; display: block;
  }
  .swoosh { left: 150px; top: 484px; width: 210px; height: 30px; }
  .map-frame {
    left: 382px; top: 334px; width: 309px; height: 191px;
    background: #fff; padding: 5px;
    box-shadow: 0 2px 6px rgba(0,0,0,0.3);
  }
  .map-area {
    width: 100%; height: 100%;
    background: linear-gradient(135deg, #eeeeea 0%, #e2e4de 60%, #d7e3ef 100%);
  }
</style>
</head>
<body>

<section class="postcard postcard--back" aria-label="Postcard back">
  <h1 class="abs brand-name">Birchway Swing Studio's</h1>
  <p class="abs brand-tagline">New indoor location is open!</p>

  <h2 class="abs offer-title">Our training facility that offers :</h2>
  <ul class="abs offer-list">
    <li>Award winner instruction</li>
    <li>State-of-the-art technology</li>
    <li>Custom club fitting</li>
  </ul>
  <p class="abs intro">Whether you are a beginner, an aspiring athlete, or an amateur, Birchway Swing Studio offers personalized programs to help take your game to the next level.</p>

  <div class="abs golfer-art" role="img" aria-label="Golf ball on a tee beside a silhouette of a golfer mid-swing"></div>
  <div class="abs red-block"></div>

  <p class="abs cta"><span class="cta-line1">Call now to schedule your</span><span class="cta-line2">free tour or to sign up</span></p>
  <p class="abs phone">555 018 2470</p>
  <p class="abs website">WWW.BIRCHWAYSWING.COM</p>
  <p class="abs note">*Limited memberships available</p>

  <div class="abs stamp" aria-label="Stamp area"></div>
  <div class="abs address-line" style="top:261px"></div>
  <div class="abs address-line" style="top:301px"></div>
  <div class="abs address-line" style="top:340px"></div>
  <div class="abs address-line" style="top:380px"></div>
</section>

<section class="postcard postcard--front" aria-label="Postcard front">
  <div class="abs grass" role="img" aria-label="Close-up photo of green golf course grass"></div>
  <div class="abs photo-strip" role="img" aria-label="Black and white photo edge of stored golf gear"></div>
  <div class="abs lawn-panel" role="img" aria-label="Golf ball sitting on a black tee against a green background"></div>
  <div class="abs scene-photo" role="img" aria-label="Black and white photo of a golfer's shoes and club beside crumpled paper and a red cup"></div>

  <svg class="abs header-band" viewBox="0 0 724 130" preserveAspectRatio="none" aria-hidden="true">
    <path d="M0 0 H724 V127 Q520 70 300 84 Q120 96 0 127 Z" fill="var(--header-red)"/>
  </svg>
  <h2 class="abs headline">Don't put away your clubs just yet!</h2>

  <p class="abs closing">
    <span class="closing-lead">The course may be closed but</span>
    <span class="closing-name">Birchway Swing Studio's</span>
    <span class="closing-tag">New indoor location is open!</span>
  </p>
  <svg class="abs swoosh" viewBox="0 0 210 30" aria-hidden="true">
    <path d="M2 26 Q100 10 208 2 Q130 20 2 28 Z" fill="#ffffff"/>
  </svg>

  <div class="abs map-frame">
    <div class="map-area" role="img" aria-label="Street map showing the studio location"></div>
  </div>
</section>

</body>
</html>
```